Book cover for publishing doctoral research about various national styles of piano playing.

I need a book cover for a publication of a doctoral research with regard to styles of piano performance characteristic to various nations.

Any images or graphics are optional, typography seems most important, but please feel free to be creative.

I attach the barcode, qsr and publisher's logo in the next few days. (Logo is still being designed).

For various reasons the size of the book is not completely decided yet. Please create your design in 7" x 10", but if at all possible, I would like to ask for files of two sizes, also including 8.5" x 11" in the final submission.

I am looking for a design that looks professional, probably simple, but I am open to any suggestions.

Dear Designers,I would like to thank you all for participation and submitting so many high-quality designs.My final decision was based on the feedback I received from my professional colleagues and potential readers.I would like to wish you all the best for the future.Best wishes,Tadeusz Added Monday, December 21, 2015

Pianists, students, music professionals

Publishing

• Title: Unfolding Seven Harbour Lullabies
• Subtitle: Memories and departures
• Author: Tadeusz Jarocki
• Space for my logo on the front page and the spine.
• On the back page, please include some space for a short biography, 'barcode' and 'qsr' code.
• Please include whatever else you consider necessary.
• Would it be possible to use the same cover to a e-book edition?

```html
<!DOCTYPE html>
<html lang="en">
<head>
<meta charset="utf-8">
<title>Unfolding Seven Harbour Lullabies — Cover</title>
<link rel="stylesheet" href="https://fonts.googleapis.com/css2?family=Cinzel:wght@400;600&family=Oswald:wght@300&display=swap">
<style>
  :root {
    --paper: #f7f7f6;
    --gold: #e9b323;
    --gold-soft: #d9a726;
    --key: #161616;
    --ink-grey: #4a4a4a;
    --white: #ffffff;
  }
  html, body {
    margin: 0;
    padding: 0;
    overflow: hidden;
    background: var(--paper);
  }
  .cover {
    position: relative;
    width: 966px;
    height: 1200px;
    overflow: hidden;
    background: var(--paper);
  }
  .cover-illustration {
    position: absolute;
    left: 230px;
    top: 200px;
    width: 460px;
    height: 340px;
    background: linear-gradient(180deg, #3a3a3a 0%, var(--key) 55%, var(--gold-soft) 100%);
    opacity: 0.92;
  }
  .title-block {
    position: absolute;
    right: 120px;
    top: 590px;
    margin: 0;
    text-align: right;
    font-family: "Cinzel", serif;
    color: var(--gold);
    line-height: 0.95;
  }
  .title-line { display: block; white-space: nowrap; }
  .title-line--lead {
    font-size: 108px;
    font-weight: 600;
    text-shadow: 0 6px 8px rgba(233, 179, 35, 0.18);
  }
  .title-line--middle { font-size: 68px; font-weight: 400; margin-top: 6px; }
  .title-line--last { font-size: 50px; font-weight: 400; margin-top: 8px; }
  .subtitle {
    display: block;
    margin-top: 16px;
    font-family: "Oswald", sans-serif;
    font-weight: 300;
    font-size: 34px;
    letter-spacing: 0.5px;
    color: var(--ink-grey);
  }
  .author-band {
    position: absolute;
    left: 230px;
    top: 962px;
    width: 560px;
    height: 58px;
    background: var(--gold);
    display: flex;
    align-items: center;
    justify-content: flex-end;
    padding-right: 34px;
    box-sizing: border-box;
  }
  .author-name {
    font-family: "Cinzel", serif;
    font-weight: 600;
    font-size: 32px;
    color: var(--white);
    letter-spacing: 0.5px;
  }
  .author-rule {
    position: absolute;
    left: 790px;
    top: 962px;
    width: 176px;
    height: 2px;
    background: var(--gold);
  }
</style>
</head>
<body>
<main class="cover">
  <div class="cover-illustration" role="img" aria-label="Illustration of black piano keys fading into gold, with thin gold lines hanging below them"></div>

  <h1 class="title-block">
    <span class="title-line title-line--lead">Unfolding</span>
    <span class="title-line title-line--middle">Seven Harbour</span>
    <span class="title-line title-line--last">Lullabies</span>
    <span class="subtitle">Memories and departures</span>
  </h1>

  <div class="author-rule"></div>
  <div class="author-band">
    <span class="author-name">Tadeusz Jarocki</span>
  </div>
</main>
</body>
</html>
```